Bright, Fun and hard to forget home inspection business card.

We need a Business card design for a new Home Inspection company. We are building a brand that is bright, fun and easy to remember.

Target Market(s)

Anyone involed in buying and selling of homes.

Industry/Entity Type

Home Inspection

Contact Information for Business Card

Colin Marlowe Owner/Inspector

Wedsite- PorchAndRafterCheck.example
Phone: 253-555-0187
Email- ColinMarlowe@mailbox.example
WA Lic # 4806

Requirements
Must have
• BRQV LOGO somewhere on card.

```html
<!DOCTYPE html>
<html lang="en">
<head>
<meta charset="utf-8">
<title>Business Card – Porch and Rafter Check</title>
<link rel="stylesheet" href="https://fonts.googleapis.com/css2?family=Play:wght@400;700&display=swap">
<style>
  :root {
    --page-bg: #d9d6d2;
    --card-bg: #efedeb;
    --ink: #3a3a3c;
    --ink-soft: #4a4a4c;
    --accent: #f0673a;
    --band-dark: #3b3b3d;
    --white: #ffffff;
  }
  * { box-sizing: border-box; margin: 0; padding: 0; }
  html, body {
    width: 1200px;
    height: 768px;
    overflow: hidden;
    background: var(--page-bg);
    font-family: "Play", sans-serif;
  }
  .card {
    position: absolute;
    left: 80px;
    top: 84px;
    width: 1040px;
    height: 600px;
    border-radius: 30px;
    background: linear-gradient(160deg, #f4f3f1 0%, var(--card-bg) 60%, #e8e5e2 100%);
    overflow: hidden;
    box-shadow: 0 10px 30px rgba(0,0,0,0.15);
  }
  .brand {
    position: absolute;
    left: 600px;
    top: 110px;
    width: 380px;
    display: flex;
    align-items: center;
    gap: 18px;
  }
  .brand-dot {
    flex: none;
    width: 56px;
    height: 56px;
    border-radius: 50%;
    background: var(--accent);
  }
  .brand-name {
    font-weight: 700;
    font-size: 40px;
    line-height: 1.05;
    color: var(--ink);
    text-transform: uppercase;
  }
  .holder-name {
    position: absolute;
    left: 44px;
    top: 188px;
    font-size: 29px;
    font-weight: 400;
    letter-spacing: 1.5px;
    color: var(--ink);
    text-transform: uppercase;
  }
  .holder-title {
    position: absolute;
    left: 44px;
    top: 246px;
    font-size: 23px;
    color: var(--accent);
  }
  .divider {
    position: absolute;
    left: 44px;
    top: 295px;
    width: 880px;
    height: 3px;
    background: linear-gradient(90deg, var(--accent) 0%, var(--accent) 70%, rgba(240,103,58,0) 100%);
  }
  .address {
    position: absolute;
    left: 44px;
    top: 392px;
    font-size: 23px;
    line-height: 34px;
    color: var(--ink-soft);
  }
  .contacts {
    position: absolute;
    right: 40px;
    top: 322px;
    list-style: none;
    text-align: right;
    color: var(--ink);
  }
  .contacts li {
    display: flex;
    justify-content: flex-end;
    align-items: center;
    gap: 14px;
  }
  .contacts .phone { font-size: 22px; letter-spacing: 1.5px; height: 50px; }
  .contacts .online { font-size: 19px; height: 36px; }
  .contacts svg { width: 22px; height: 22px; flex: none; }
  .band-accent {
    position: absolute;
    left: 420px;
    right: 0;
    bottom: 0;
    height: 41px;
    background: var(--accent);
  }
  .band-dark {
    position: absolute;
    left: 0;
    bottom: 0;
    width: 450px;
    height: 60px;
  }
  .band-dark svg { display: block; }
  .band-web {
    position: absolute;
    left: 44px;
    bottom: 16px;
    font-size: 20px;
    letter-spacing: 0.5px;
    color: var(--white);
  }
</style>
</head>
<body>
  <main class="card">
    <div class="brand">
      <span class="brand-dot"></span>
      <span class="brand-name">Porch and Rafter Check</span>
    </div>

    <h1 class="holder-name">Colin Marlowe</h1>
    <p class="holder-title">Owner/Inspector</p>
    <div class="divider"></div>

    <p class="address">Licensed Home Inspector<br>WA Lic # 4806</p>

    <ul class="contacts">
      <li class="phone">253-555-0187
        <svg viewBox="0 0 24 24" aria-hidden="true"><path fill="#f0673a" d="M6.6 10.8c1.4 2.8 3.8 5.1 6.6 6.6l2.2-2.2c.3-.3.7-.4 1-.2 1.1.4 2.3.6 3.6.6.6 0 1 .4 1 1V20c0 .6-.4 1-1 1C10.6 21 3 13.4 3 4c0-.6.4-1 1-1h3.5c.6 0 1 .4 1 1 0 1.3.2 2.5.6 3.6.1.3 0 .7-.2 1z"/></svg>
      </li>
      <li class="phone">253-555-0142
        <svg viewBox="0 0 24 24" aria-hidden="true"><rect x="6" y="1.5" width="12" height="21" rx="2" fill="none" stroke="#f0673a" stroke-width="2"/><rect x="8" y="4.5" width="8" height="12" fill="#f0673a"/><circle cx="12" cy="19.5" r="1.2" fill="#f0673a"/></svg>
      </li>
      <li class="phone">253-555-0163
        <svg viewBox="0 0 24 24" aria-hidden="true"><rect x="3" y="9" width="18" height="12" rx="1.5" fill="#f0673a"/><rect x="7" y="3" width="10" height="7" fill="#f0673a"/><rect x="6" y="12" width="7" height="2" fill="#efedeb"/><rect x="6" y="16" width="3" height="2" fill="#efedeb"/><rect x="11" y="16" width="3" height="2" fill="#efedeb"/></svg>
      </li>
      <li class="online">ColinMarlowe@mailbox.example
        <svg viewBox="0 0 24 24" aria-hidden="true"><rect x="2" y="5" width="20" height="14" rx="1" fill="#f0673a"/><path d="M2.5 5.5 12 13l9.5-7.5" fill="none" stroke="#efedeb" stroke-width="1.6"/></svg>
      </li>
      <li class="online">PorchAndRafterCheck.example
        <svg viewBox="0 0 24 24" aria-hidden="true"><g fill="none" stroke="#f0673a" stroke-width="1.8"><circle cx="12" cy="12" r="9.5"/><ellipse cx="12" cy="12" rx="4" ry="9.5"/><path d="M2.5 12h19M4 7h16M4 17h16"/></g></svg>
      </li>
    </ul>

    <div class="band-accent"></div>
    <div class="band-dark">
      <svg width="450" height="60" viewBox="0 0 450 60" aria-hidden="true">
        <path d="M0 0H395c18 0 28 8 36 24l19 36H0z" fill="#3b3b3d"/>
      </svg>
    </div>
    <p class="band-web">PorchAndRafterCheck.example</p>
  </main>
</body>
</html>
```